BRISKA sparkling water needs new artwork! Based in Southern California

"Briska" is a new sparkling water company based in Southern California that offers refreshing flavors (lime, cherry, & mango) with B vitamins and antioxidants.

We would like to see packaging designs for standard 12oz cans for each of the three flavors.
Our initial preference is to have individual artwork for each flavor.

Attached are examples of competitors' designs.
Updates

We are extending the deadline for the Thanksgiving Holiday. Thank you all for your contributions.

```html
<!DOCTYPE html>
<html lang="en">
<head>
<meta charset="utf-8">
<title>Briska Sparkling Water – Can Labels</title>
<link rel="stylesheet" href="https://fonts.googleapis.com/css2?family=Oswald:wght@500;600&family=Barlow:wght@400;500;600&display=swap">
<style>
  :root {
    --bg: #e0e0df;
    --white: #ffffff;
    --lime-1: #00a54f;
    --lime-2: #6cb945;
    --lime-3: #b0d13d;
    --mango-1: #f04f23;
    --mango-2: #f58a24;
    --mango-3: #fbb72a;
    --cherry-1: #8c1c30;
    --cherry-2: #b52147;
    --cherry-3: #e0306a;
  }
  * { margin: 0; padding: 0; box-sizing: border-box; }
  html, body {
    width: 960px;
    height: 1200px;
    overflow: hidden;
    background: var(--bg);
  }
  .label-set {
    position: absolute;
    top: 342px;
    left: 25px;
    display: flex;
    gap: 35px;
  }
  .label {
    position: relative;
    width: 280px;
    height: 515px;
    overflow: hidden;
    color: var(--white);
    text-align: center;
  }
  .label__pattern {
    position: absolute;
    inset: 0;
  }
  .label--lime .label__pattern {
    background:
      radial-gradient(circle at 25% 20%, var(--lime-3) 0, transparent 40%),
      radial-gradient(circle at 80% 75%, var(--lime-1) 0, transparent 45%),
      radial-gradient(circle at 85% 15%, var(--lime-1) 0, transparent 35%),
      linear-gradient(160deg, var(--lime-2), var(--lime-3) 50%, var(--lime-2));
  }
  .label--mango .label__pattern {
    background:
      radial-gradient(circle at 85% 12%, var(--mango-1) 0, transparent 35%),
      radial-gradient(circle at 30% 35%, var(--mango-3) 0, transparent 45%),
      radial-gradient(circle at 70% 80%, var(--mango-3) 0, transparent 40%),
      linear-gradient(160deg, var(--mango-2), var(--mango-3) 50%, var(--mango-2));
  }
  .label--cherry .label__pattern {
    background:
      radial-gradient(circle at 70% 8%, var(--cherry-1) 0, transparent 30%),
      radial-gradient(circle at 25% 60%, var(--cherry-3) 0, transparent 45%),
      radial-gradient(circle at 80% 35%, var(--cherry-3) 0, transparent 40%),
      linear-gradient(160deg, var(--cherry-2), var(--cherry-3) 50%, var(--cherry-2));
  }
  .label__brand,
  .label__type,
  .label__flavor,
  .label__benefits,
  .label__volume {
    position: absolute;
    left: 0;
    right: 0;
  }
  .label__brand {
    top: 188px;
    font-family: "Barlow", sans-serif;
    font-weight: 600;
    font-size: 58px;
    line-height: 1;
  }
  .label__type {
    top: 260px;
    font-family: "Oswald", sans-serif;
    font-weight: 600;
    font-size: 14px;
    letter-spacing: 1.6px;
  }
  .label__flavor {
    top: 351px;
    font-family: "Barlow", sans-serif;
    font-weight: 500;
    font-size: 18px;
    letter-spacing: 5px;
    padding-left: 5px;
  }
  .label__benefits {
    top: 391px;
    font-family: "Barlow", sans-serif;
    font-weight: 400;
    font-size: 9.5px;
    line-height: 1;
  }
  .label__volume {
    top: 470px;
    font-family: "Oswald", sans-serif;
    font-weight: 500;
    font-size: 15px;
    letter-spacing: -0.2px;
  }
</style>
</head>
<body>
  <main class="label-set">
    <section class="label label--lime">
      <div class="label__pattern" role="img" aria-label="Decorative pattern of rounded teardrop shapes in greens"></div>
      <div class="label__brand">Briska</div>
      <div class="label__type">SPARKLING WATER</div>
      <div class="label__flavor">LIME</div>
      <div class="label__benefits">with B vitamins<br>&amp; antioxidants</div>
      <div class="label__volume">12oz | 350ml</div>
    </section>

    <section class="label label--mango">
      <div class="label__pattern" role="img" aria-label="Decorative pattern of rounded teardrop shapes in oranges and yellows"></div>
      <div class="label__brand">Briska</div>
      <div class="label__type">SPARKLING WATER</div>
      <div class="label__flavor">MANGO</div>
      <div class="label__benefits">with B vitamins<br>&amp; antioxidants</div>
      <div class="label__volume">12oz | 350ml</div>
    </section>

    <section class="label label--cherry">
      <div class="label__pattern" role="img" aria-label="Decorative pattern of rounded teardrop shapes in pinks and deep reds"></div>
      <div class="label__brand">Briska</div>
      <div class="label__type">SPARKLING WATER</div>
      <div class="label__flavor">CHERRY</div>
      <div class="label__benefits">with B vitamins<br>&amp; antioxidants</div>
      <div class="label__volume">12oz | 350ml</div>
    </section>
  </main>
</body>
</html>
```